Sports Nutrition Business Background template

My business KOVARA is all about sports nutrition.

www.kovara.com.au

Put simply, KOVARA works with clients to optimize behavioral, attitudinal and dietary habits to help surpass the individuals health and fitness goals. Im looking for something that is a template. I am going to use this for a series of programs I am running, so I will be reusing it multiple times for many different programs, I would like it to appeal to both men and women.

Id like it simple, happy, friendly and approachable please! Can the form factor be for “Facebook cover photos”

Here are a few ideas I had in mind.
https://cdn-pics-b.lumorahost.example/imgs-prv1/t22.0-4/8837261_20481736492017733_4728391056_o.jpg

https://cdn-pics-c.lumorahost.example/imgs-prv2/t22.0-4/8839104_20481755310298833_3917264502_o.jpg

I like the simplicity and approach-ability of both designs. They are brightly colored and it works well. I am thinking of having my logo in place of the guys picture and also having pictures of myself on the side faded into the background like this

http://www.brivantide.com/wp-content/uploads/2013/09/Male-Fitness-Models-BAck.jpg

Industry/Entity Type

Fitness

```html
<!DOCTYPE html>
<html lang="en">
<head>
<meta charset="utf-8">
<title>Intimate One-on-One Sessions – Cover</title>
<link rel="stylesheet" href="https://fonts.googleapis.com/css2?family=Anton&family=Oswald:wght@700&family=Archivo+Black&family=Roboto:ital,wght@1,900&display=swap">
<style>
  :root {
    --page: #ffffff;
    --sky-top: #6f9fd6;
    --sky-mid: #cfe2f2;
    --sea: #4fb8c4;
    --sand: #ece6dc;
    --panel-green: #86bd33;
    --band-yellow: #f3e33f;
    --title-white: #ffffff;
    --title-yellow: #f4e23a;
    --tagline-green: #3d6a1f;
    --people-tone-a: #d9a27e;
    --people-tone-b: #6e7462;
    --arm-light: #a7d84a;
    --arm-dark: #2f7a2c;
  }
  * { margin: 0; padding: 0; box-sizing: border-box; }
  html, body {
    width: 1200px; height: 1000px; overflow: hidden;
    background: var(--page);
  }
  .canvas { position: relative; width: 1200px; height: 1000px; }
  .cover {
    position: absolute; left: 0; top: 277px;
    width: 1200px; height: 445px; overflow: hidden;
  }
  .beach-scene {
    position: absolute; inset: 0;
    background: linear-gradient(180deg,
      var(--sky-top) 0%, var(--sky-mid) 22%, #eef4f8 38%,
      var(--sea) 48%, #a9d9d8 62%, var(--sand) 78%, var(--sand) 100%);
  }
  .program-panel {
    position: absolute; left: 375px; top: 80px;
    width: 780px; height: 288px;
  }
  .program-panel .band {
    position: absolute; left: 0; top: 225px; width: 100%; height: 63px;
    background: var(--band-yellow);
    border-radius: 0 0 16px 0;
  }
  .program-panel .panel {
    position: absolute; left: 0; top: 0; width: 100%; height: 243px;
    background: var(--panel-green);
    border-radius: 0 16px 16px 0;
  }
  .headline {
    position: absolute; left: 100px; top: 8px; width: 400px;
    text-align: center;
    text-shadow: 2px 3px 3px rgba(0,0,0,0.35);
  }
  .headline .line-intimate {
    display: block;
    font-family: "Anton", sans-serif;
    font-size: 86px; line-height: 96px;
    letter-spacing: 4px; color: var(--title-white);
  }
  .headline .line-one {
    display: block;
    font-family: "Oswald", sans-serif; font-weight: 700;
    font-size: 56px; line-height: 60px;
    letter-spacing: 1px; color: var(--title-yellow);
  }
  .headline .line-sessions {
    display: block;
    font-family: "Archivo Black", sans-serif;
    font-size: 48px; line-height: 62px;
    letter-spacing: 11px; color: var(--title-white);
    margin-right: -11px;
  }
  .tagline {
    position: absolute; left: 60px; top: 248px;
    font-family: "Roboto", sans-serif; font-style: italic; font-weight: 900;
    font-size: 22px; letter-spacing: 1.6px;
    color: var(--tagline-green);
  }
  .trainers-photo {
    position: absolute; left: 0; top: 24px; width: 485px; height: 421px;
    background: linear-gradient(90deg, var(--people-tone-a) 0%, var(--people-tone-b) 45%, var(--people-tone-a) 75%, rgba(217,162,126,0) 100%);
    border-radius: 40px 40px 0 0;
    opacity: 0.9;
  }
  .flex-arm-illustration {
    position: absolute; left: 910px; top: 25px; width: 272px; height: 280px;
    background: radial-gradient(circle at 45% 45%, var(--arm-light) 0%, var(--arm-dark) 70%, rgba(47,122,44,0) 100%);
    border-radius: 50%;
  }
</style>
</head>
<body>
<div class="canvas">
  <section class="cover">
    <div class="beach-scene" role="img" aria-label="Tropical beach with blue sky, clouds, turquoise sea and sand"></div>
    <div class="program-panel">
      <div class="band"></div>
      <div class="panel"></div>
      <h1 class="headline">
        <span class="line-intimate">INTIMATE</span>
        <span class="line-one">ONE-ON-ONE</span>
        <span class="line-sessions">SESSIONS</span>
      </h1>
      <p class="tagline">One of the biggest challenges you will face!</p>
    </div>
    <div class="trainers-photo" role="img" aria-label="Three smiling fitness trainers posing on the beach"></div>
    <div class="flex-arm-illustration" role="img" aria-label="Green leafy illustration of a flexed arm"></div>
  </section>
</div>
</body>
</html>
```